Norwegian psychologist service needs a fresh and exiting web site*

Norwegian psychologist service: working with therapy, personal development, mastery and personal growth. Focus: children and teenagers with special needs; family dynamics; group processes; individuals with a need for therapy and personal growth. (Our company name: Fjordlys og samhold (means Mastery and Growth).

We already have a logo for the company, which will be used (will be attached in the project).

The webside is to be structured in 4 pages with roll down curtain menus (the numbers are just for guiding the designer - the should not be added):

Page 1: Om Fjordlys og Samhold (about Mastery and Growth): this is where our business is is presented/described shortly: Lorem Ipsum dolor cit...

Page 2: Tjenester (Services): this is where our 5 service areas are presented:
2.1 Utredning (Investigation, diagnosing): Lorem Ipsum dolor cit...
2.2 Rådgivning (consulting): Lorem Ipsum dolor cit...

2.3 Kurs og work shops (courses and work shops): Lorem Ipsum dolor cit...
2.3a Fjordlys og samhold Tema 1 (T1)
2.3b Fjordlys og samhold Tema 2 (T2)
2.3c Fjordlys og samhold Tema 3 (T3)

2.4 Terapi og utvikling (Therapy and development)
2.4a Fjordlys og samhold for individer (FS1)
2.4b Fjordlys og samhold i familier (FS2)
2.4c Fjordlys og samhold i grupper (FS3)
2.4d Fjordlys og samhold i institusjoner (FS4)

Page 3: Aktuelt (Blog): this is our blog where we share knowledge and articles

Page 4: Kontakt (Contact): This is the contact form page. Contact form should constitute:
- Ditt navn (your name)
- E-post (your e-mail)
- Emne (subject)
- Melding (message/description)

Our project should also include suggestion for handheld units (iPhone, iPad).
Updates

We have both been traveling with work for a while, and then unfortunately both of us got sick on return, so we need a few more days to evaluate and choose design. Kind Regards Arvid & Margit

Target Market(s)

Focus on therapy, learning, mastery and growth for children and teenagers with special needs, within the family dynamics, or in a group setting.
OUR MARKETS:
Private market: individuals, families, groups and health industry institutions (with focus on learning, mastery, growth (as well as growing up) and psychiatry for children and teenagers with special difficulties and needs)
Public institutions: Government institutions, state institutions and municipality institutions (e.g. schools, municipality health service, hospitals) that serve the public (families with children and teenagers with special needs, and where learning, mastery, growth (as well as growing up) and potential psychiatry is an issue).

Number of Pages Required

4 page

Font styles to use
Sans Serif

Colors

Designer to choose colors to be used in the design.

Requirements
Must have
• The website must have 4 pages with roll down curtain menus (we have added a PDF with suggested structure, and headings, with sub menus - see attached PDF drawing.
• The web page must also use the added logo file - and make the web page work well with our logo.
• We would like the website to have a modern look and we would like the site to be associated with typical HIGH END TOP QUALITY private health institutions, but with a stronger focus on human beings (hands, faces etc), and not white coats and doctors. We are psychologists in the private market.
• For instance, if photos are being used - we tend to like "warm" almost art-like, "grainy" two-tone (e.g. sepia) photos to illustrate our focus. If designer can find such photos as part of design, it would be interesting to us. We would like a few photos like that integrated in the design.
• We also want a design suggestion for how the web page should look like and behave on handheld units (e.g. iPhone, iPad).
Nice to have
• If designer could find a number of suitable photos that matches the business idea and design requirements (see description above), that could follow website, that would be good.
• It could also be nice to have graphic symbols that denote the different pages/subpages (subjects)....
• HORSES: we sometimes use horses as a "tool" in therapy sessions. The horse is not necessarily used for riding, but for contact, communication and grooming. PHOTOS: we would like the designer to find an opportunity for using a photo reflecting this cooperation between therapist, child, teenager and horse. It is a bit up to the designer to find a way to do this... Since the horse is only a tool, among many other tools, it does not have to be much - but we want to try and see how it will work with a photo that also reflects this part of our business.

```html
<!DOCTYPE html>
<html lang="en">
<head>
<meta charset="utf-8">
<title>About Us – Fjordlys og samhold</title>
<link href="https://fonts.googleapis.com/css2?family=Montserrat:wght@400;500;700&display=swap" rel="stylesheet">
<style>
  :root {
    --rose: #c8628a;
    --teal: #62b8ae;
    --ink: #2f2f35;
    --navy: #2c3a8c;
    --paper: #ffffff;
  }
  * { box-sizing: border-box; margin: 0; padding: 0; }
  html, body { width: 1200px; height: 946px; overflow: hidden; background: var(--paper); }
  body { font-family: "Montserrat", Arial, sans-serif; color: var(--ink); position: relative; }

  .site-header {
    position: absolute; top: 0; left: 128px; width: 944px; height: 50px;
    display: flex; align-items: center; justify-content: space-between;
  }
  .brand { display: flex; align-items: center; gap: 6px; margin-left: 8px; }
  .brand-dot { width: 12px; height: 12px; border-radius: 50%; background: var(--navy); }
  .brand-name { font-size: 11px; font-weight: 500; color: var(--navy); letter-spacing: .2px; }

  .nav { display: flex; gap: 25px; list-style: none; }
  .nav a { font-size: 10px; font-weight: 500; color: var(--ink); text-decoration: none; letter-spacing: .2px; }
  .nav a.is-active { color: var(--rose); font-weight: 700; }

  .page-title {
    position: absolute; top: 102px; left: 128px;
    font-size: 37px; font-weight: 700; color: var(--rose);
  }
  .intro {
    position: absolute; top: 162px; left: 128px; width: 944px;
    font-size: 15px; line-height: 21.3px;
  }
  .intro p + p { margin-top: 21px; }

  .hero-photo {
    position: absolute; top: 393px; left: 128px; width: 944px; height: 369px;
    background:
      radial-gradient(ellipse 22% 60% at 30% 60%, #ece9e6 0%, rgba(236,233,230,0) 70%),
      linear-gradient(90deg, #6f5a48 0%, #a89b8e 20%, #b8ada3 50%, #c2b8ad 75%, #a48b73 100%);
  }

  .cta {
    position: absolute; top: 793px; left: 859px; width: 213px; height: 50px;
    display: flex; align-items: center; justify-content: center;
    background: var(--teal); color: #fff; border-radius: 3px;
    font-size: 16px; font-weight: 700; text-decoration: none;
  }

  .site-footer {
    position: absolute; top: 907px; left: 128px; width: 944px; height: 20px;
    display: flex; align-items: center; justify-content: space-between;
  }
  .social { display: flex; gap: 12px; list-style: none; }
  .social li { width: 13px; height: 13px; border-radius: 50%; background: var(--rose); }
  .footer-nav { display: flex; gap: 25px; list-style: none; }
  .footer-nav a { font-size: 10px; font-weight: 500; color: var(--rose); text-decoration: none; letter-spacing: .2px; }
</style>
</head>
<body>
  <header class="site-header">
    <div class="brand">
      <span class="brand-dot"></span>
      <span class="brand-name">Fjordlys og samhold</span>
    </div>
    <ul class="nav">
      <li><a class="is-active" href="#">ABOUT</a></li>
      <li><a href="#">SERVICES</a></li>
      <li><a href="#">BLOG</a></li>
      <li><a href="#">CONTACT</a></li>
    </ul>
  </header>

  <h1 class="page-title">About Us</h1>

  <section class="intro">
    <p>Norwegian psychologist service: working with therapy, personal development, mastery and personal growth.<br>
    Focus: children and teenagers with special needs; family dynamics; group processes; individuals with a need for therapy and personal growth.</p>
    <p>Lorem ipsum dolor sit amet, consectetur adipiscing elit. Suspendisse rhoncus, lectus at convallis egestas, magna diam suscipit nisl, eget fringilla nisl tortor vitae nisi. Ut enim diam, fermentum eu elit quis, vehicula mollis odio. Mauris in suscipit sapien. Sed vitae odio sed neque rutrum varius. Mauris sagittis arcu massa. Sed ultrices eget quam a egestas. Proin scelerisque ac ante vitae fringilla. Morbi libero leo, ultricies eu commodo a, ultrices vel quam. Duis tristique nunc massa, et pulvinar lacus convallis eget.</p>
  </section>

  <div class="hero-photo" role="img" aria-label="Photo of a psychologist in a white shirt seated in a bright therapy room with children's drawings and toy shelves"></div>

  <a class="cta" href="#">Contact Us</a>

  <footer class="site-footer">
    <ul class="social" aria-label="Social links">
      <li></li><li></li><li></li><li></li>
    </ul>
    <ul class="footer-nav">
      <li><a href="#">ABOUT</a></li>
      <li><a href="#">SERVICES</a></li>
      <li><a href="#">BLOG</a></li>
      <li><a href="#">CONTACT</a></li>
    </ul>
  </footer>
</body>
</html>
```